Full Page Appliance Ad

Create a full page ad (7.5" W x 10" H) representing that we are a full service appliance company, where we have a showroom located at 14 N. Birch Lane Marrowdale, OR 97999. Our website is www.qrtolvek.com , and our phone number is 555-555-0148. We don't only sell appliances, we deliver, install, and service. We also offer an additional year warranty* (see store for details). In addition to appliances, we also have an Electrical Department that specializes in residential applications.
May be best if split the full page ad into two spots. One spot to reference appliances, and the other to represent electrical.
I want it to look clean, and not too busy
Target Market(s)
30-70 years old
Look and feel

```html
<!DOCTYPE html>
<html lang="en">
<head>
<meta charset="UTF-8">
<title>Qrtolvek and Son Inc – Full Page Ad</title>
<link href="https://fonts.googleapis.com/css2?family=Poppins:wght@400;500;600;700&display=swap" rel="stylesheet">
<style>
  :root {
    --navy: #13284f;
    --navy-mid: #1d3566;
    --contact-blue: #34508a;
    --gold: #f2b631;
    --page: #f4f4f4;
    --backdrop: #d9d9d9;
    --ink: #13284f;
    --white: #ffffff;
    --rule: #2f4776;
  }
  * { box-sizing: border-box; margin: 0; padding: 0; }
  html, body { width: 1200px; height: 1117px; overflow: hidden; }
  body { background: var(--backdrop); font-family: "Poppins", sans-serif; color: var(--ink); }

  .ad {
    position: absolute; left: 210px; top: 38px;
    width: 780px; height: 1040px;
    background: var(--page); overflow: hidden;
  }
  .intro-panel {
    position: absolute; left: 0; top: 0; width: 340px; height: 330px;
    background: var(--navy); color: var(--white);
    padding: 60px 24px 0 36px;
  }
  .brand { display: flex; align-items: center; gap: 14px; }
  .brand-mark { width: 50px; height: 50px; border-radius: 50%; border: 3px solid var(--white); flex: none; }
  .brand-name { font-weight: 600; font-size: 24px; line-height: 1.1; color: var(--white); letter-spacing: 0.5px; }
  .divider { height: 2px; background: var(--rule); margin: 36px 0 26px; }
  .headline { font-weight: 700; font-size: 22px; line-height: 1.2; }
  .headline .accent { color: var(--gold); display: block; }
  .showroom { font-weight: 400; font-size: 16px; line-height: 1.3; margin-top: 8px; }

  .appliance-photo {
    position: absolute; left: 360px; top: 0; width: 420px; height: 330px;
    background: linear-gradient(160deg, #e9eaec 0%, #c6c9cd 60%, #9ea2a7 100%);
  }

  .roof { position: absolute; left: 0; width: 780px; }
  .roof-top { top: 300px; height: 160px; }
  .roof-bottom { top: 690px; height: 110px; }

  .services { position: absolute; left: 40px; top: 422px; }
  .services .lead { font-size: 15px; font-weight: 400; }
  .services .strong { font-size: 22px; font-weight: 700; line-height: 1.15; }

  .warranty-bar {
    position: absolute; left: 0; top: 482px; width: 600px; height: 34px;
    background: var(--navy); color: var(--white);
    font-size: 14px; font-weight: 600; padding: 7px 0 0 40px; white-space: nowrap;
  }
  .warranty-bar .note { color: var(--gold); }

  .kitchen-row {
    position: absolute; left: 12px; top: 530px; width: 756px; height: 150px;
    display: grid; grid-template-columns: repeat(4, 1fr); gap: 8px;
  }
  .kitchen-photo { height: 150px; }
  .kitchen-photo.wood { background: linear-gradient(135deg, #d9d6d2, #8a5a3a 70%, #5a3c2a); }
  .kitchen-photo.blue { background: linear-gradient(135deg, #eef0f2, #3f5b99 60%, #c7a57e); }
  .kitchen-photo.open { background: linear-gradient(135deg, #f4f4f2, #c9c3b8 60%, #6b6257); }
  .kitchen-photo.grey { background: linear-gradient(135deg, #e6e8ea, #a9aeb5 60%, #7d838b); }

  .electrician-photo {
    position: absolute; left: 20px; top: 740px; width: 400px; height: 235px;
    background: linear-gradient(135deg, #f1f2f3 0%, #cfd4da 55%, #7a8aa6 80%, #e2462c 100%);
  }
  .web-bar {
    position: absolute; left: 20px; top: 975px; width: 400px; height: 65px;
    background: var(--gold); display: flex; align-items: center; justify-content: center; gap: 10px;
    font-size: 22px; font-weight: 700; color: var(--navy);
  }
  .electrical-copy {
    position: absolute; left: 440px; top: 812px; width: 330px;
    font-size: 17px; font-weight: 500; line-height: 1.3; white-space: nowrap;
  }
  .contact-box {
    position: absolute; left: 420px; top: 905px; width: 360px; height: 135px;
    background: var(--contact-blue); color: var(--white); padding: 30px 0 0 32px;
  }
  .contact-box .label { font-size: 22px; font-weight: 500; }
  .contact-box .phone { display: flex; align-items: center; gap: 10px; font-size: 31px; font-weight: 700; white-space: nowrap; }
</style>
</head>
<body>
  <main class="ad">
    <section class="intro-panel">
      <div class="brand">
        <span class="brand-mark"></span>
        <span class="brand-name">QRTOLVEK<br>AND SON INC</span>
      </div>
      <div class="divider"></div>
      <h1 class="headline">We are a full service <span class="accent">appliance company,</span></h1>
      <p class="showroom">where we have a showroom<br>located at 14 N. Birch Lane<br>Marrowdale, OR 97999</p>
    </section>

    <div class="appliance-photo" role="img" aria-label="Stainless steel appliances: refrigerator, wall oven, cooktop, range hood and dishwasher"></div>

    <svg class="roof roof-top" viewBox="0 0 780 160" aria-hidden="true">
      <polygon points="0,0 340,0 340,40 150,20 0,85" fill="var(--navy)"/>
      <polygon points="150,0 780,70 780,92 150,20" fill="var(--navy)"/>
      <polygon points="0,85 150,20 780,92 780,117 150,46 0,112" fill="var(--gold)"/>
    </svg>

    <div class="services">
      <p class="lead">We don't only sell appliances,</p>
      <p class="strong">we deliver, install, and service.</p>
    </div>

    <div class="warranty-bar">We also offer an additional year warranty* <span class="note">(see store for details)</span></div>

    <div class="kitchen-row">
      <div class="kitchen-photo wood" role="img" aria-label="Modern kitchen with wood cabinets and stainless appliances"></div>
      <div class="kitchen-photo blue" role="img" aria-label="Kitchen with blue cabinets and an island"></div>
      <div class="kitchen-photo open" role="img" aria-label="Open-plan kitchen with a large island"></div>
      <div class="kitchen-photo grey" role="img" aria-label="Minimal grey kitchen with built-in oven"></div>
    </div>

    <svg class="roof roof-bottom" viewBox="0 0 780 110" aria-hidden="true">
      <polygon points="20,75 190,0 780,55 780,78 190,22 20,98" fill="var(--navy-mid)"/>
      <polygon points="550,42 780,0 780,60" fill="var(--gold)"/>
    </svg>

    <div class="electrician-photo" role="img" aria-label="Electrician working in a residential breaker panel with pliers"></div>

    <p class="electrical-copy">In addition to appliances,<br>we also have an Electrical<br>Department that specializes<br>in residential applications.</p>

    <div class="contact-box">
      <p class="label">Contact us</p>
      <p class="phone">
        <svg width="28" height="28" viewBox="0 0 24 24" aria-hidden="true"><circle cx="12" cy="12" r="12" fill="var(--gold)"/><path d="M8.2 6.5l1.8-.4 1 2.6-1.2 1a7 7 0 0 0 3.2 3.2l1-1.2 2.6 1-.4 1.8c-.2.6-.8 1-1.4.9A9 9 0 0 1 7.3 7.9c0-.7.3-1.2.9-1.4z" fill="var(--contact-blue)"/></svg>
        555-555-0148.
      </p>
    </div>

    <div class="web-bar">
      <svg width="20" height="20" viewBox="0 0 20 20" aria-hidden="true"><circle cx="10" cy="10" r="9" fill="var(--navy)"/><g fill="none" stroke="var(--gold)" stroke-width="1.2"><circle cx="10" cy="10" r="6"/><ellipse cx="10" cy="10" rx="2.6" ry="6"/><line x1="4" y1="10" x2="16" y2="10"/></g></svg>
      www.qrtolvek.com
    </div>
  </main>
</body>
</html>
```